" A empresa em questao será uma clínica médica e de fisioterapia especializada em tratamento de coluna. Tanto os médicos quanto os tratamentos fisioterápicos (fisioterapia, osteopatia, RPG) serao direcionados para o público que busca tratamento e soluçoes para dores nas costas em geral. "

```html
<!DOCTYPE html>
<html lang="pt-BR">
<head>
<meta charset="utf-8">
<title>Instituto Eixo Vital – Cartão de visita</title>
<link rel="stylesheet" href="https://fonts.googleapis.com/css2?family=Open+Sans:wght@300;400&display=swap">
<style>
  :root {
    --page-bg: #ecebe8;
    --card-dark: #0b0b0b;
    --card-light: #ffffff;
    --brand-teal: #5cc6d1;
    --ink-light: #ffffff;
    --mark-grey: #b9bcbf;
    --label-grey: #8d9296;
  }
  * { margin: 0; padding: 0; box-sizing: border-box; }
  html, body {
    width: 1200px;
    height: 1200px;
    overflow: hidden;
    background: var(--page-bg);
    font-family: "Open Sans", Arial, sans-serif;
  }
  .canvas { position: relative; width: 1200px; height: 1200px; }

  .card {
    position: absolute;
    width: 696px;
    height: 408px;
    border-radius: 36px;
    overflow: hidden;
    box-shadow: 0 6px 18px rgba(0,0,0,0.18);
  }

  /* Front */
  .card--front {
    left: 228px;
    top: 168px;
    background: var(--card-dark);
    display: flex;
    align-items: center;
    justify-content: center;
  }
  .brand-lockup { display: flex; align-items: center; gap: 26px; margin-left: 10px; }
  .brand-dot {
    width: 94px; height: 94px;
    border-radius: 50%;
    background: var(--mark-grey);
  }
  .brand-rule { width: 2px; height: 118px; background: var(--ink-light); }
  .brand-name {
    color: var(--ink-light);
    font-weight: 300;
    font-size: 38px;
    line-height: 1.12;
  }
  .brand-name .kicker { display: block; font-size: 38px; }

  /* Back */
  .card--back {
    left: 247px;
    top: 612px;
    background: var(--card-light);
    display: grid;
    grid-template-columns: 212px 1fr;
  }
  .back-brand {
    display: flex;
    align-items: center;
    justify-content: center;
    padding: 0 24px;
    color: var(--label-grey);
    font-weight: 300;
    font-size: 26px;
    line-height: 1.2;
    text-align: center;
  }
  .back-info {
    background: var(--brand-teal);
    color: var(--ink-light);
    text-align: right;
    padding: 62px 24px 0 0;
    font-weight: 400;
  }
  .person-name { font-size: 23px; line-height: 1.35; }
  .person-role { font-size: 23px; line-height: 1.35; }
  .contact { margin-top: 38px; font-size: 22px; line-height: 1.4; }
  .address { margin-top: 58px; font-size: 14px; line-height: 1.45; }
</style>
</head>
<body>
<main class="canvas">
  <section class="card card--front" aria-label="Frente do cartão">
    <div class="brand-lockup">
      <div class="brand-dot" aria-hidden="true"></div>
      <div class="brand-rule" aria-hidden="true"></div>
      <p class="brand-name"><span class="kicker">Instituto</span>Eixo Vital</p>
    </div>
  </section>

  <section class="card card--back" aria-label="Verso do cartão">
    <div class="back-brand">Instituto Eixo Vital</div>
    <div class="back-info">
      <p class="person-name">Nome Sobrenome</p>
      <p class="person-role">Função</p>
      <div class="contact">
        <p>(00)0000-0000</p>
        <p>contato@eixovital.com.br</p>
      </div>
      <div class="address">
        <p>Rua Sem Nome,00</p>
        <p>Bairro Sem Nome</p>
        <p>Cidade Sem Nome</p>
      </div>
    </div>
  </section>
</main>
</body>
</html>
```